Book cover for book entitled "Planting Gardens After Winter ....Plus Growing Bright Mornings Within"

I need a book cover for ebook and 6" x 9" paperback print book (print forge pod). I want a simple but "positive" cover with no gothic or darkness in design. I would prefer a "hopeful color scheme" in yellow, blue, green analogous colors and very easy to read main title "Planting Gardens After Winter". I want the tag line of the title. "plus grow bright mornings within" included on the cover please. I am not opposed to white in the color scheme I believe the graphic needs to somehow deal with doors, blocks, keys (perhaps a combination lock since the book is my story of healing from pancreatic cancer through faith, nutrition, and lifestyle changes). I am basically looking for the front cover from you but in a high definition format so it can be transferred to posters and banners for seminar displays. I am uploading my photo in case a designer would want to include a small copy of it in a design although I plan the photo to be on the back cover. The photo could, of course, be cropped.

I would also be interested in seeing a design with a woman  with arms folded and looking satisfied or victorious (happy) casually leaning against a closed door.    It can be very simple....

This graphic could be photo or drawing-even a good line drawing.   Almost whimsical would be okay.  This cover need not be highly complicated but I do want the title easy to read in small or large sizes for ebook and print book.

Reason: I have just changed to "committed" and some new "acceptances" have just come in.

Industry/Entity Type

Nutrition

Font styles to use
Serif

Colors
fbee3e
acd037
33b7a4
34a6d8
3377b5

```html
<!DOCTYPE html>
<html lang="en">
<head>
<meta charset="utf-8">
<title>Planting Gardens After Winter — Book Cover</title>
<link rel="stylesheet" href="https://fonts.googleapis.com/css2?family=Crimson+Pro:ital,wght@0,600;0,700;1,600&display=swap">
<style>
  :root {
    --page-bg: #ffffff;
    --sky-deep: #3377b5;
    --sky: #34a6d8;
    --meadow: #acd037;
    --meadow-deep: #7fae2e;
    --sun: #fbee3e;
    --door-edge: rgba(98, 78, 62, 0.82);
    --band: rgba(112, 112, 112, 0.80);
    --text-light: #ffffff;
    --text-shadow: rgba(0, 0, 0, 0.45);
  }
  * { margin: 0; padding: 0; box-sizing: border-box; }
  html, body { width: 1200px; height: 1000px; overflow: hidden; background: var(--page-bg); }
  .canvas { position: relative; width: 1200px; height: 1000px; }
  .cover {
    position: absolute; left: 335px; top: 80px; width: 558px; height: 832px;
    overflow: hidden; font-family: "Crimson Pro", Georgia, serif; color: var(--text-light);
  }
  .cover-art {
    position: absolute; inset: 0;
    background:
      radial-gradient(ellipse 62% 52% at 52% 50%, rgba(0,0,0,0) 55%, var(--door-edge) 100%),
      radial-gradient(circle at 22% 14%, rgba(251,238,62,0.55) 0%, rgba(251,238,62,0) 30%),
      linear-gradient(180deg, var(--sky-deep) 0%, var(--sky) 38%, var(--meadow) 68%, var(--meadow-deep) 100%);
  }
  .author-band {
    position: absolute; left: 0; top: 0; width: 308px; height: 72px;
    background: var(--band); clip-path: polygon(0 0, 100% 0, 84% 100%, 0 100%);
  }
  .author-name {
    position: absolute; left: 30px; top: 25px; font-size: 26px; font-weight: 700; letter-spacing: 0.3px;
  }
  .title {
    position: absolute; left: 0; right: 0; top: 228px; text-align: center;
    font-weight: 700; line-height: 0.86; text-shadow: 0 2px 8px var(--text-shadow);
  }
  .title span { display: block; }
  .title-planting { font-size: 104px; }
  .title-gardens { font-size: 98px; }
  .title-after { font-size: 132px; }
  .title-winter { font-size: 134px; font-style: italic; font-weight: 600; letter-spacing: 2px; margin-top: 4px; }
  .tagline-band {
    position: absolute; left: 40px; right: 0; bottom: 0; height: 74px;
    background: var(--band); clip-path: polygon(0 0, 100% 0, 100% 100%, 9% 100%);
  }
  .tagline {
    position: absolute; right: 34px; bottom: 24px; font-size: 27px; font-weight: 700; letter-spacing: 0.3px;
  }
</style>
</head>
<body>
<div class="canvas">
  <div class="cover">
    <div class="cover-art" role="img" aria-label="Photo of a wooden door with a heart-shaped opening and keyhole revealing bright blue sky and a green meadow"></div>
    <div class="author-band"></div>
    <p class="author-name">Marla Whitfield</p>
    <h1 class="title">
      <span class="title-planting">Planting</span>
      <span class="title-gardens">Gardens</span>
      <span class="title-after">After</span>
      <span class="title-winter">Winter</span>
    </h1>
    <div class="tagline-band"></div>
    <p class="tagline">plus grow bright mornings within</p>
  </div>
</div>
</body>
</html>
```